Consulting Company PowerPoint Template Design

We are looking for an updated PowerPoint template design or our 55 person energy consulting firm (K7) based in San Francisco (www.kayseven.example). We would like two versions of the same PowerPoint template in a 16:9 and 4:3 format with our existing logo.

We have an existing color scheme and template and are seeking your help to polish/update the template design for wide format and create a flexible template that is easy to use with content from Excel and Word. Our current template, and a couple of examples that we like are attached.

Specific requests include:

• Dark background for slide title
• A narrow section header
• Maximizing white space for content
• A limited number of well designed Master template layouts to choose from
• A selection of title and section header slides that are not San Francisco specific with some variety to chose from ideally with a focus on energy or nature, graphics/visuals.

For examples of energy specific templates see:
https://www.brightslidery.example/energy/powerpoint-templates/0.html

Requirements
Must have
• Must use our logo but open to other designs, fonts, and styles for the PowerPoint template.
• Please use our existing color scheme found in the attached Excel file.
• Also we would like the ability to easily copy and paste from our existing/original template to the new template. In other words we would like backward compatibility to apply the new template format to our old PowerPoints that use our existing template.

```html
<!DOCTYPE html>
<html lang="en">
<head>
<meta charset="utf-8">
<title>What We Do – K7</title>
<link rel="stylesheet" href="https://fonts.googleapis.com/css2?family=Open+Sans:wght@400;600;700&display=swap">
<style>
  :root {
    --navy: #3b4861;
    --text-grey: #6f737a;
    --subtitle-grey: #b9bcc2;
    --stripe-blue: #1d5c9c;
    --sun-gold: #d9a944;
    --photo-light: #ecdcb8;
    --photo-mid: #d2b887;
    --photo-dark: #b5986a;
    --accent-blue: #1f9ae6;
    --accent-navy: #3c4a64;
    --accent-green: #79b544;
    --accent-lime: #a7d34d;
    --white: #ffffff;
  }
  * { margin: 0; padding: 0; box-sizing: border-box; }
  html, body { width: 1200px; height: 674px; overflow: hidden; background: var(--white); }
  body { font-family: "Open Sans", Arial, sans-serif; }
  .slide { position: relative; width: 1200px; height: 674px; overflow: hidden; background: var(--white); }
  .hero-art { position: absolute; left: 0; top: 0; width: 1200px; height: 674px; }
  .heading { position: absolute; left: 700px; width: 480px; text-align: center; }
  .heading__title { margin-top: 52px; font-size: 35px; font-weight: 700; color: var(--navy); letter-spacing: 0.5px; }
  .heading__subtitle { margin-top: 4px; font-size: 14px; color: var(--subtitle-grey); }
  .service { position: absolute; display: flex; align-items: flex-start; }
  .service__badge { flex: none; width: 72px; height: 72px; border-radius: 50%; display: flex; align-items: center; justify-content: center; }
  .service__badge svg { width: 34px; height: 34px; }
  .service__body { margin-left: 24px; width: 430px; }
  .service__name { font-size: 15px; font-weight: 700; color: var(--navy); line-height: 1; }
  .service__text { margin-top: 14px; font-size: 15px; line-height: 1.7; color: var(--text-grey); }
  .service--improve { left: 648px; top: 158px; }
  .service--improve .service__badge { background: var(--accent-blue); }
  .service--rebrand { left: 616px; top: 286px; }
  .service--rebrand .service__badge { background: var(--accent-navy); }
  .service--success { left: 582px; top: 408px; }
  .service--success .service__badge { background: var(--accent-green); }
  .service--growth { left: 550px; top: 536px; }
  .service--growth .service__badge { background: var(--accent-lime); }
  .service__badge + .service__body { padding-top: 4px; }
</style>
</head>
<body>
<main class="slide">
  <svg class="hero-art" viewBox="0 0 1200 674" aria-hidden="false">
    <defs>
      <linearGradient id="photoTone" x1="0" y1="0" x2="1" y2="1">
        <stop offset="0" stop-color="var(--photo-dark)"/>
        <stop offset="0.45" stop-color="var(--photo-mid)"/>
        <stop offset="1" stop-color="var(--photo-light)"/>
      </linearGradient>
    </defs>
    <polygon role="img" aria-label="Photo of a field of solar panels under a hazy sky, warm sepia tone"
             points="0,0 652,0 504,674 0,674" fill="url(#photoTone)"/>
    <rect x="0" y="0" width="652" height="5" fill="var(--sun-gold)"/>
    <polygon class="diagonal-stripe" points="652,0 664,0 532,674 504,674" fill="var(--stripe-blue)"/>
  </svg>

  <header class="heading">
    <h1 class="heading__title">WHAT WE DO?</h1>
    <p class="heading__subtitle">Your Subtitle Here</p>
  </header>

  <section class="service service--improve">
    <div class="service__badge">
      <svg viewBox="0 0 34 34" fill="none" stroke="var(--white)" stroke-width="2">
        <rect x="5" y="6" width="24" height="17" rx="1"/>
        <line x1="17" y1="3" x2="17" y2="6"/>
        <line x1="17" y1="23" x2="12" y2="30"/>
        <line x1="17" y1="23" x2="22" y2="30"/>
        <polyline points="10,18 15,13 19,16 24,11"/>
      </svg>
    </div>
    <div class="service__body">
      <h2 class="service__name">IMPROVE</h2>
      <p class="service__text">Refers to a good or service being offered by a company ideally a product</p>
    </div>
  </section>

  <section class="service service--rebrand">
    <div class="service__badge">
      <svg viewBox="0 0 34 34" fill="none" stroke="var(--white)" stroke-width="2">
        <path d="M7 19v-3a10 10 0 0 1 20 0v3"/>
        <rect x="5" y="18" width="5" height="8" rx="2"/>
        <rect x="24" y="18" width="5" height="8" rx="2"/>
        <path d="M26 26c0 3-4 4-8 4"/>
      </svg>
    </div>
    <div class="service__body">
      <h2 class="service__name">REBRAND</h2>
      <p class="service__text">Refers to a good or service being offered by a company ideally a product</p>
    </div>
  </section>

  <section class="service service--success">
    <div class="service__badge">
      <svg viewBox="0 0 34 34" fill="none" stroke="var(--white)" stroke-width="2">
        <circle cx="17" cy="12" r="6"/>
        <path d="M6 29c1-6 6-9 11-9s10 3 11 9z"/>
      </svg>
    </div>
    <div class="service__body">
      <h2 class="service__name">SUCCESS</h2>
      <p class="service__text">Refers to a good or service being offered by a company ideally a product</p>
    </div>
  </section>

  <section class="service service--growth">
    <div class="service__badge">
      <svg viewBox="0 0 34 34" fill="none" stroke="var(--white)" stroke-width="2">
        <circle cx="17" cy="12" r="6"/>
        <path d="M6 29c1-6 6-9 11-9s10 3 11 9z"/>
      </svg>
    </div>
    <div class="service__body">
      <h2 class="service__name">SUCCESS</h2>
      <p class="service__text">Refers to a good or service being offered by a company ideally a product</p>
    </div>
  </section>
</main>
</body>
</html>
```